creation of business cards for Velmora Sàrl

Velmora S% 26 # 224; rl is a soci% 26 # 233; t% 26 # 233; consultancy that accompanies companies in the development of their business on the market% 26 # 233; Switzerland by providing strategic contacts or market information; and by providing administrative or logistical support. Our consulting skills focus on sectors% 26 # 224; high value added% 26 # 233; e, such as trade in food goods% 26 # 39amp; drinks, fashion% 26amp; lifestyle, products and services for% 26 # 233; s in high-tech industries (pharmaceutical, chemical, m% 26 # 233; pricy 26% 23 #; cision) or sustainable solutions (% 26 # 233; energies renewable, mat% 26 # 233; recyclable materials). As part of the launch of our activity% 26 # 233;, we need% 26 # 39;% 26 # 233; to establish business cards to d% 26 # 233; work our new customers (Swiss or international).

Target Market(s)

Companies wishing to develop their activity% 26 # 233; s in Switzerland or% 26 # 224; l% 26 # 39;% 26 # 233; abroad (mainly in Europe).

Contact Information for Business Card

Prénom NOM
Velmora Sàrl
Bureau de Lavertin
Rue des Tilleuls 14, 2000 Neuchâtel
Tél. : 032 718 46 39
info@velmora-conseil.ch
www.velmora-conseil.ch

Font styles to use
Serif
Sans Serif

Colors

Designer to choose colors to be used in the design.

Requirements
Must have
• The logo The name of the company% 26 # 233; t% 26 # 233; (Velmora S% 26 # 224; rl) One field for the mailing address One field for the number% 26 # 233; ro de t% 26 # 233; l% 26 # 233; phone One field for the % 26 # 39; email address and website

```html
<!DOCTYPE html>
<html lang="fr">
<head>
<meta charset="utf-8">
<title>Velmora Sàrl – Carte de visite</title>
<link rel="stylesheet" href="https://fonts.googleapis.com/css2?family=Arimo:wght@400;700&family=Exo+2:wght@300&display=swap">
<style>
  :root {
    --page-bg: #e9ebee;
    --card-top: #f7f7f8;
    --card-top-edge: #ececee;
    --accent-stripe: #a9b9c7;
    --navy: #1b3a50;
    --on-navy: #ffffff;
  }
  html, body {
    margin: 0;
    width: 1200px;
    height: 900px;
    overflow: hidden;
    background: var(--page-bg);
  }
  .business-card {
    position: absolute;
    left: 150px;
    top: 171px;
    width: 900px;
    height: 558px;
    box-shadow: 0 14px 40px rgba(20, 40, 60, 0.18);
    overflow: hidden;
  }
  .brand-area {
    position: absolute;
    left: 0; top: 0;
    width: 100%;
    height: 280px;
    background: linear-gradient(180deg, var(--card-top) 0%, var(--card-top-edge) 100%);
  }
  .brand-mark {
    position: absolute;
    left: 178px;
    top: 116px;
    width: 83px;
    height: 83px;
    border-radius: 14px;
    background: var(--navy);
  }
  .brand-name {
    position: absolute;
    left: 306px;
    top: 108px;
    margin: 0;
    font-family: "Exo 2", sans-serif;
    font-weight: 300;
    font-size: 68px;
    line-height: 1;
    letter-spacing: 6px;
    color: var(--navy);
  }
  .accent-stripe {
    position: absolute;
    left: 0; top: 280px;
    width: 100%;
    height: 9px;
    background: var(--accent-stripe);
  }
  .contact-area {
    position: absolute;
    left: 0; top: 289px;
    width: 100%;
    height: 269px;
    background: var(--navy);
    color: var(--on-navy);
    font-family: "Arimo", sans-serif;
    text-align: center;
  }
  .contact-area p { margin: 0; position: absolute; left: 0; width: 100%; }
  .person-name { top: 42px; font-size: 33px; letter-spacing: 0.5px; }
  .contact-line { top: 105px; font-size: 24px; }
  .contact-line b { font-weight: 700; }
  .company-name { top: 155px; font-size: 24px; font-weight: 700; }
  .company-address { top: 189px; font-size: 24px; }
</style>
</head>
<body>
  <section class="business-card">
    <div class="brand-area">
      <div class="brand-mark"></div>
      <h1 class="brand-name">VELMORA</h1>
    </div>
    <div class="accent-stripe"></div>
    <div class="contact-area">
      <p class="person-name">PRENOM NOM</p>
      <p class="contact-line"><b>P:</b> 032 718 46 39 | <b>E:</b> info@velmora-conseil.ch | www.velmora-conseil.ch</p>
      <p class="company-name">VELMORA SARL</p>
      <p class="company-address">Bureau de Lavertin Rue des Tilleuls 14, 2000 Neuchâtel</p>
    </div>
  </section>
</body>
</html>
```